Italian restaurant needs new site

Need to make our website better.

Must have reservation module

Must be able to sell wine tasting tours and wine pairing tours and intégrate with lumo desk

Blog

Social media

Wandermeter ranking and last review.

Number of Pages Required

1 page

Font styles to use
Serif

Requirements
Must have
• Reservation module
• Marketplace to buy wine pairings and gift certificates
• Wandermeter review
• Chatterbay posts
• All info from old site

```html
<!DOCTYPE html>
<html lang="en">
<head>
<meta charset="utf-8">
<title>Vellora Bistro – Italian Cuisine &amp; Wine Bar</title>
<link rel="stylesheet" href="https://fonts.googleapis.com/css2?family=Montserrat:wght@400;500;600;700&family=Pinyon+Script&display=swap">
<style>
:root{
  --red:#9c1b20;
  --red-dark:#6e1216;
  --ink:#222;
  --muted:#777;
  --line:#d9d9d9;
  --night:#151515;
  --gold:#d8a21b;
  --white:#fff;
}
*{box-sizing:border-box;margin:0;padding:0}
html,body{width:1200px;height:4167px;overflow:hidden}
body{position:relative;font-family:"Montserrat",sans-serif;color:var(--ink);background:var(--white)}
.abs{position:absolute}
.ph{position:absolute;display:block}

/* hero */
.hero{position:absolute;left:0;top:0;width:1200px;height:556px;background:radial-gradient(ellipse at 60% 55%,#6b4a3c 0%,#2c1d19 45%,#0d0b0b 100%)}
.nav{position:absolute;top:20px;left:556px;display:flex;gap:28px;font-size:13px;font-weight:500;color:var(--white);letter-spacing:.5px}
.brand{position:absolute;left:40px;top:70px;width:200px;color:var(--white);text-align:center}
.brand-name{font-size:40px;font-weight:500;letter-spacing:3px;line-height:1}
.brand-sub{font-size:26px;letter-spacing:6px;margin-top:6px}
.brand-tag{font-size:11px;letter-spacing:2px;margin-top:10px;border-top:1px solid var(--white);padding-top:6px}
.btn-ghost{position:absolute;left:100px;width:125px;height:34px;border:1px solid var(--white);color:var(--white);font-size:11px;font-weight:600;display:flex;align-items:center;justify-content:center;letter-spacing:.5px}
.socials{position:absolute;display:flex;gap:12px}
.socials span{width:24px;height:24px;border:1px solid currentColor;border-radius:50%}
.hero-title{position:absolute;left:520px;top:200px;width:660px;text-align:center;font-family:"Pinyon Script",cursive;font-size:66px;line-height:1.15;color:var(--white)}

/* about */
.about-text{position:absolute;left:150px;top:612px;width:640px;font-size:12.5px;line-height:2;color:var(--muted);text-align:center}
.about-text p+p{margin-top:16px}
.about-panel{position:absolute;left:868px;top:556px;width:332px;height:402px;background:linear-gradient(135deg,#8e1a1f,#5c1013)}
.section-mark{display:flex;align-items:center;justify-content:center;gap:0;margin-top:12px}
.section-mark i{display:block;width:70px;height:2px;background:currentColor}
.section-mark b{display:block;width:8px;height:8px;background:currentColor;transform:rotate(45deg)}
.panel-title{position:absolute;width:100%;text-align:center;color:var(--white);font-size:44px;font-weight:500}

/* gallery */
.gallery{position:absolute;left:0;top:958px;width:1200px;height:439px;background:linear-gradient(90deg,#1b1b1b,#2e2a28 50%,#1b1b1b)}

/* tours */
.card{position:absolute;top:1445px;width:310px;height:347px;border:1px solid var(--line);background:var(--white)}
.card-title{position:absolute;left:12px;top:192px;font-size:15px;font-weight:600;color:var(--red)}
.stars{position:absolute;font-size:13px;letter-spacing:1px;color:var(--gold)}
.stars .off{color:#ccc}
.card-meta{position:absolute;font-size:12px;color:var(--muted)}
.price{position:absolute;right:16px;top:240px;font-size:26px;font-weight:600;color:var(--gold)}
.btn-outline{position:absolute;left:78px;top:292px;width:155px;height:34px;border:1px solid var(--red);color:var(--red);font-size:12px;font-weight:600;display:flex;align-items:center;justify-content:center}

/* pairing */
.pairing{position:absolute;left:0;top:1833px;width:1200px;height:237px;background:linear-gradient(90deg,#2a2623,#111 70%,#1c1c1c)}
.pairing-list{position:absolute;left:0;top:0;width:361px;height:237px;background:#f7f5f3}
.pairing-list ul{list-style:none;position:absolute;left:146px;top:30px;font-size:13px;color:var(--muted);line-height:36px}
.pairing-list li:first-child{color:var(--gold)}

/* menus */
.h-center{position:absolute;width:1200px;text-align:center;font-size:22px;font-weight:500;color:var(--red)}
.tabs{position:absolute;left:417px;top:2182px;display:flex}
.tabs span{height:34px;display:flex;align-items:center;justify-content:center;font-size:13px;font-weight:600;color:var(--white);background:#b24549;padding:0 22px;border-right:1px solid #d07a7d}
.tabs span.on{background:var(--red)}
.menu-col{position:absolute;width:486px}
.menu-col h3{font-size:19px;font-weight:600;color:var(--red);margin-bottom:14px;letter-spacing:.5px}
.menu-col h4{font-size:12px;font-weight:600;color:var(--ink);margin:12px 0 6px}
.row{display:flex;align-items:baseline;font-size:12.5px;line-height:25px;color:var(--ink)}
.row .dots{flex:1;border-bottom:1px dotted var(--red);margin:0 6px;transform:translateY(-4px)}
.row .amt{font-weight:500}

/* booking */
.booking{position:absolute;left:0;top:2708px;width:1200px;height:445px;background:linear-gradient(180deg,#7a7a7a,#4c4c4c 60%,#5e5e5e)}
.book-box{position:absolute;left:250px;top:2814px;width:847px;height:317px;background:var(--white)}
.field{position:absolute;left:33px;width:261px;height:32px;border:1px solid var(--line)}
.btn-red{position:absolute;background:var(--red);color:var(--white);font-size:13px;font-weight:600;display:flex;align-items:center;justify-content:center}

/* reviews */
.rating-name{position:absolute;left:40px;top:3190px;font-size:26px;font-weight:600;color:var(--ink)}
.review{position:absolute;top:3170px;width:190px;text-align:center;font-size:11px;color:var(--muted)}
.review .avatar{width:44px;height:44px;border-radius:50%;background:#b9b9b9;margin:0 auto 8px}
.review q{display:block;color:var(--red);font-size:14px;margin-top:4px;quotes:none}

/* blog */
.blog{position:absolute;left:0;top:3306px;width:1200px;height:347px;background:linear-gradient(90deg,#8b8a86,#c9c3b8 50%,#8c8f94)}
.post{position:absolute;top:3342px;width:310px;height:290px;background:var(--white)}
.post h5{position:absolute;left:12px;top:176px;font-size:14.5px;font-weight:500;color:var(--ink)}
.post p{position:absolute;left:12px;top:202px;width:285px;font-size:11.5px;line-height:17px;color:var(--muted)}
.arrow{position:absolute;font-size:34px;color:var(--white);font-weight:300}

/* hours */
.hours{position:absolute;left:111px;top:3767px;width:978px;border-collapse:collapse;font-size:11.5px;color:var(--muted);text-align:center}
.hours th,.hours td{border:1px solid var(--line);height:30px;font-weight:400}
.hours th.on{background:var(--red);color:var(--white)}

/* footer */
.footer{position:absolute;left:0;top:3917px;width:1200px;height:222px;background:var(--red)}
.contact{position:absolute;left:850px;top:3948px;color:var(--white);font-size:13px;line-height:20px}
.contact .item{display:flex;gap:16px;margin-bottom:16px}
.copyright{position:absolute;left:145px;top:4146px;font-size:11px;color:var(--red)}
</style>
</head>
<body>

<!-- hero -->
<header class="hero">
  <div class="ph" style="left:0;top:0;width:1200px;height:556px;background:radial-gradient(ellipse at 70% 60%,rgba(180,120,90,.35),transparent 60%)" role="img" aria-label="Candlelit restaurant dining room with set tables"></div>
  <nav class="nav"><span>HOME</span><span>MENUS</span><span>GALLERY</span><span>BOOK ONLINE</span><span>CONTACT US</span></nav>
  <div class="brand">
    <div class="brand-name">VELLORA</div>
    <div class="brand-sub">BISTRO</div>
    <div class="brand-tag">ITALIAN CUISINE &amp; WINE BAR</div>
  </div>
  <div class="btn-ghost" style="top:328px">SEE THE MENU</div>
  <div class="btn-ghost" style="top:383px">BOOK A TABLE</div>
  <div class="socials" style="left:78px;top:478px;color:#fff"><span></span><span></span><span></span><span></span><span></span></div>
  <h1 class="hero-title">Vellora Bistro italian Restaurant in Cabo San Lucas</h1>
</header>

<!-- about -->
<section>
  <div class="about-text">
    <p>Vellora Bistro sits in the heart of downtown, across from Corso Plaza, just two short blocks up from Marbrisa Resort and the marina. It is a place with a great original Southern Italian and Mediterranean cuisine and a European touch. Come to enjoy your classic favorites or try the most distinctive plates on our menu, a variety of homemade, fresh cooked dishes derived from generations-old family recipes, accompanied by an extensive selection of national and international wines and fine Italian inspired cocktails.</p>
    <p>Local residents Matteo Ravelli and Luca Ferrante have joined forces with Bay Drift Tours to create this unique and contemporary dining experience in a comfortable, lively and stylish atmosphere great for locals and visitors.</p>
  </div>
  <div class="about-panel" role="img" aria-label="Red toned photo of wine glasses">
    <div class="panel-title" style="top:168px">About us<div class="section-mark"><i></i><b></b><i></i></div></div>
  </div>
</section>

<!-- gallery -->
<section class="gallery">
  <div class="abs" style="left:88px;top:168px;color:#fff;font-size:44px;font-weight:500">Gallery<div class="section-mark" style="justify-content:flex-start;margin-left:20px"><i></i><b></b><i></i></div></div>
  <div class="ph" style="left:408px;top:22px;width:412px;height:200px;background:linear-gradient(135deg,#6d5b4c,#2f2822)" role="img" aria-label="Restaurant interior with tables"></div>
  <div class="ph" style="left:820px;top:22px;width:208px;height:410px;background:linear-gradient(160deg,#5a3d2a,#9a3a22 55%,#c86b2a)" role="img" aria-label="Chillies, vegetables and wooden spoon"></div>
  <div class="ph" style="left:408px;top:222px;width:208px;height:210px;background:linear-gradient(135deg,#7a5c46,#3a2c22)" role="img" aria-label="Guests dining together"></div>
  <div class="ph" style="left:616px;top:222px;width:204px;height:210px;background:linear-gradient(135deg,#3b3230,#6e4a35)" role="img" aria-label="Chef plating a steak dish"></div>
</section>

<!-- tours -->
<section>
  <article class="card" style="left:111px">
    <div class="ph" style="left:0;top:0;width:308px;height:180px;background:linear-gradient(135deg,#8a6a45,#4a3522)" role="img" aria-label="Wine barrels in a cellar"></div>
    <div class="card-title">Wine Tour In France</div>
    <div class="stars" style="left:12px;top:218px">★★<span class="off">★★★</span></div>
    <div class="card-meta" style="left:90px;top:220px">51 Reviews</div>
    <div class="card-meta" style="left:12px;top:252px">◷ &nbsp;3 hours</div>
    <div class="price">250$</div>
    <div class="btn-outline">VIEW DETAIL</div>
  </article>
  <article class="card" style="left:444px">
    <div class="ph" style="left:0;top:0;width:308px;height:180px;background:linear-gradient(135deg,#8a8a8a,#3a3a3a)" role="img" aria-label="Rows of oak wine barrels"></div>
    <div class="card-title">Wine Tour In France</div>
    <div class="stars" style="left:12px;top:218px">★★<span class="off">★★★</span></div>
    <div class="card-meta" style="left:90px;top:220px">51 Reviews</div>
    <div class="card-meta" style="left:12px;top:252px">◷ &nbsp;3 hours</div>
    <div class="price">250$</div>
    <div class="btn-outline">VIEW DETAIL</div>
  </article>
  <article class="card" style="left:780px">
    <div class="ph" style="left:0;top:0;width:308px;height:180px;background:linear-gradient(135deg,#3a1a14,#8c2a1c 60%,#c0642a)" role="img" aria-label="Red wine poured into a glass"></div>
    <div class="card-title">Wine Tour In France</div>
    <div class="stars" style="left:12px;top:218px">★★<span class="off">★★★</span></div>
    <div class="card-meta" style="left:90px;top:220px">51 Reviews</div>
    <div class="card-meta" style="left:12px;top:252px">◷ &nbsp;3 hours</div>
    <div class="price">250$</div>
    <div class="btn-outline">VIEW DETAIL</div>
  </article>
</section>

<!-- pairing -->
<section class="pairing">
  <div class="pairing-list">
    <ul><li>Chocolate Wine</li><li>Red Wine Card</li><li>Dessert Wine</li><li>Ocean Madison Red Wine</li><li>Pasabella Allegra Red Wine</li></ul>
  </div>
  <div class="ph" style="left:397px;top:45px;width:261px;height:150px;background:linear-gradient(135deg,#6b4a32,#c9a878 60%,#8a5a3a)" role="img" aria-label="Cheese board with wine and fruit"></div>
  <div class="abs" style="left:680px;top:48px;color:#fff;font-size:16px">Chocolate Wine</div>
  <div class="abs" style="left:680px;top:78px;color:var(--gold);font-size:17px;font-weight:500">25$</div>
  <div class="btn-ghost" style="left:680px;top:128px;width:100px;height:32px">BUY NOW</div>
  <div class="abs" style="left:920px;top:85px;width:240px;text-align:center;color:#fff;font-size:24px;font-weight:600;line-height:1.4;letter-spacing:1px">BEST WINE<br>PAIRING GUIDE</div>
</section>

<!-- menus -->
<section>
  <h2 class="h-center" style="top:2100px">Menus<div class="section-mark" style="color:var(--red);margin-top:6px"><i style="width:50px"></i><b></b><i style="width:50px"></i></div></h2>
  <div class="tabs"><span class="on">Dinner</span><span>Lunch</span><span>Truffle Set Menu</span></div>

  <div class="menu-col" style="left:111px;top:2240px">
    <h3>APPETIZER</h3>
    <div class="row"><span>Buffalo Chicken Dip</span><span class="dots"></span><span class="amt">20$</span></div>
    <div class="row"><span>Pepper Poppers</span><span class="dots"></span><span class="amt">35$</span></div>
    <div class="row"><span>Glazed Chicken Wings</span><span class="dots"></span><span class="amt">29$</span></div>
    <div class="row"><span>Cucumber Stuffed Cherry Tomatoes</span><span class="dots"></span><span class="amt">22$</span></div>
    <div class="row"><span>Honey-Garlic Glazed Meatballs</span><span class="dots"></span><span class="amt">21$</span></div>
    <div class="row"><span>Savory Party Bread</span><span class="dots"></span><span class="amt">23$</span></div>
    <div class="row"><span>Avocado Salsa</span><span class="dots"></span><span class="amt">24$</span></div>
    <div class="row"><span>Pesto Pinwheels</span><span class="dots"></span><span class="amt">20$</span></div>
    <h3 style="margin-top:30px">STARTERS</h3>
    <div class="row"><span>Best caprese salad</span><span class="dots"></span><span class="amt">14$</span></div>
    <div class="row"><span>Tomato and basil salad</span><span class="dots"></span><span class="amt">15$</span></div>
    <div class="row"><span>Bagna cauda</span><span class="dots"></span><span class="amt">12$</span></div>
    <div class="row"><span>Grilled Prawn Caesar Salad Skewers</span><span class="dots"></span><span class="amt">14$</span></div>
  </div>

  <div class="menu-col" style="left:614px;top:2240px;width:475px">
    <h3>DINNER</h3>
    <h4 style="margin-top:0">PRIMI</h4>
    <div class="row"><span>Pappardelle with beef shin ragu</span><span class="dots"></span><span class="amt">20$</span></div>
    <div class="row"><span>Spaghetti alla chitarra with red mullet puttanesca</span><span class="dots"></span><span class="amt">35$</span></div>
    <div class="row"><span>Tajarin with black truffles &amp; parmesan</span><span class="dots"></span><span class="amt">29$</span></div>
    <div class="row"><span>Pumpkin &amp; ricotta tortellini with burnt butter &amp; sage</span><span class="dots"></span><span class="amt">22$</span></div>
    <h4>SECONDI</h4>
    <div class="row"><span>Pan roasted mulloway, chargrilled cos, bottarga</span><span class="dots"></span><span class="amt">14$</span></div>
    <div class="row"><span>Nettle, taleggio &amp; walnut fatagine</span><span class="dots"></span><span class="amt">15$</span></div>
    <div class="row"><span>Skirt steak with braised green beans &amp; anchovy</span><span class="dots"></span><span class="amt">12$</span></div>
    <h4>CONTORNI</h4>
    <div class="row"><span>Fried potatoes, rosemary</span><span class="dots"></span><span class="amt">14$</span></div>
    <div class="row"><span>Shaved sprouts, pecorino, mint</span><span class="dots"></span><span class="amt">15$</span></div>
    <div class="row"><span>Mixed leaf salad</span><span class="dots"></span><span class="amt">12$</span></div>
    <div class="row"><span>Braised cannellini</span><span class="dots"></span><span class="amt">12$</span></div>
  </div>
</section>

<!-- booking -->
<section class="booking" role="img" aria-label="Dimmed restaurant interior with chairs and tables">
  <h2 class="abs" style="left:0;top:48px;width:1200px;text-align:center;color:#fff;font-size:22px;font-weight:600;letter-spacing:1px">BOOK A TABLE<div class="section-mark" style="margin-top:8px"><i style="width:40px"></i><b></b><i style="width:40px"></i></div></h2>
</section>
<form class="book-box">
  <div class="field" style="top:32px"></div>
  <div class="field" style="top:80px"></div>
  <div class="field" style="top:130px"></div>
  <div class="field" style="top:180px"></div>
  <div class="btn-red" style="left:83px;top:252px;width:158px;height:32px">Check Availability</div>
  <div class="ph" style="left:300px;top:0;width:547px;height:317px;background:radial-gradient(ellipse at 55% 55%,#d8342a 0%,#e7e2d4 45%,#fafafa 80%)" role="img" aria-label="Caprese salad with tomato, mozzarella and basil"></div>
</form>

<!-- reviews -->
<section>
  <div class="abs" style="left:40px;top:3180px;display:flex;align-items:center;gap:10px">
    <span style="width:22px;height:22px;border-radius:50%;background:var(--ink);display:block"></span>
    <span style="font-size:22px;font-weight:600;color:var(--ink)">Wandermeter</span>
  </div>
  <div class="abs" style="left:60px;top:3225px;font-size:16px;font-weight:600;color:var(--red)">Vellora Bistro</div>
  <div class="abs" style="left:360px;top:3180px;width:180px;text-align:center;font-size:11px;color:var(--muted);line-height:16px">
    Wandermeter Traveler Rating<br><span style="color:var(--gold);font-size:14px">★★</span><span style="color:#ccc;font-size:14px">★★★</span><br>Wandermeter Ranking<br>#9 of 572<br><span style="color:var(--ink)">places to eat in Cabo San Lucas</span>
  </div>
  <div class="abs" style="left:612px;top:3198px;font-size:30px;color:var(--ink)">‹</div>
  <div class="review" style="left:650px"><div class="avatar"></div>Jul 21, 2017<q>"Delicious Italian"</q></div>
  <div class="abs" style="left:852px;top:3170px;width:1px;height:90px;background:var(--line)"></div>
  <div class="review" style="left:873px"><div class="avatar"></div>Jul 21, 2017<q>"Our Landlord"</q></div>
  <div class="abs" style="left:1072px;top:3198px;font-size:30px;color:var(--ink)">›</div>
</section>

<!-- blog -->
<section class="blog" role="img" aria-label="Blurred desk with notebooks and stationery"></section>
<div class="arrow" style="left:55px;top:3440px">‹</div>
<div class="arrow" style="left:1125px;top:3440px">›</div>
<article class="post" style="left:111px">
  <div class="ph" style="left:0;top:0;width:310px;height:164px;background:linear-gradient(135deg,#3b8fc4,#e4c23a 55%,#d64a3a)" role="img" aria-label="Colourful blog illustration on a desk"></div>
  <h5>Cras egestas ac nisl sit amet tincidunt</h5>
  <p>Proin lacinia orci eu justo aliquet, non mattis lorem ornare. Proin eu erat neque. Donec aliquet dictum nibh, at volutpat nisl convallis sed. Etiam ut dui iaculis.</p>
</article>
<article class="post" style="left:447px">
  <div class="ph" style="left:0;top:0;width:303px;height:164px;background:linear-gradient(135deg,#d8cdbb,#8a7058)" role="img" aria-label="Notebook and pen on a wooden table"></div>
  <h5>Cras egestas ac nisl sit amet tincidunt</h5>
  <p>Proin lacinia orci eu justo aliquet, non mattis lorem ornare. Proin eu erat neque. Donec aliquet dictum nibh, at volutpat nisl convallis sed. Etiam ut dui iaculis.</p>
</article>
<article class="post" style="left:780px">
  <div class="ph" style="left:0;top:0;width:310px;height:164px;background:linear-gradient(135deg,#c9bfae,#5a5a5a)" role="img" aria-label="Cooking blog open on a laptop"></div>
  <h5>Cras egestas ac nisl sit amet tincidunt</h5>
  <p>Proin lacinia orci eu justo aliquet, non mattis lorem ornare. Proin eu erat neque. Donec aliquet dictum nibh, at volutpat nisl convallis sed. Etiam ut dui iaculis.</p>
</article>

<!-- opening hours -->
<section>
  <h2 class="h-center" style="top:3692px;font-size:21px;font-weight:600">OPENING HOURS<div class="section-mark" style="color:var(--red);margin-top:6px"><i style="width:40px"></i><b></b><i style="width:40px"></i></div></h2>
  <table class="hours">
    <tr><th class="on">Inside</th><th>Monday</th><th>Tuesday</th><th>Wednesday</th><th>Thursday</th><th>Friday</th><th>Saturday</th><th>Sunday</th></tr>
    <tr><td>Lunch</td><td>12:00 pm - 2:45 pm</td><td>12:00 pm - 2:45 pm</td><td>12:00 pm - 2:45 pm</td><td>12:00 pm - 2:45 pm</td><td>12:00 pm - 2:45 pm</td><td>12:00 pm - 2:45 pm</td><td>12:00 pm - 2:45 pm</td></tr>
    <tr><td>Dinner</td><td>6:00 pm - 8:15 pm</td><td>6:00 pm - 8:15 pm</td><td>6:00 pm - 8:15 pm</td><td>6:00 pm - 8:15 pm</td><td>6:00 pm - 8:15 pm</td><td>6:00 pm - 8:15 pm</td><td>6:00 pm - 8:15 pm</td></tr>
  </table>
</section>

<!-- footer -->
<footer class="footer">
  <div class="ph" style="left:0;top:0;width:560px;height:222px;background:linear-gradient(135deg,#e8eef2,#cfd9e0);clip-path:polygon(0 0,100% 0,84% 100%,0 100%)" role="img" aria-label="Street map of the restaurant location"></div>
  <div class="abs" style="left:535px;top:48px;width:190px;text-align:center;color:#fff">
    <div style="font-size:34px;font-weight:500;letter-spacing:3px;line-height:1">VELLORA</div>
    <div style="font-size:22px;letter-spacing:5px;margin-top:4px">BISTRO</div>
    <div style="font-size:9.5px;letter-spacing:1.5px;margin-top:8px;border-top:1px solid #fff;padding-top:5px">ITALIAN CUISINE &amp; WINE BAR</div>
  </div>
</footer>
<address class="contact" style="font-style:normal">
  <div class="item"><svg width="14" height="18" viewBox="0 0 14 18"><path d="M7 0a7 7 0 0 0-7 7c0 5 7 11 7 11s7-6 7-11a7 7 0 0 0-7-7zm0 10a3 3 0 1 1 0-6 3 3 0 0 1 0 6z" fill="#fff"/></svg><span>18 Harbour Lane, Eastfield,<br>Coastline State,<br>Country 4021</span></div>
  <div class="item"><svg width="16" height="16" viewBox="0 0 16 16"><path d="M3 1l3 3-2 2c1 2 3 4 5 5l2-2 3 3-2 3C7 15 1 9 1 3z" fill="#fff"/></svg><span>(01) 2345 6789</span></div>
  <div class="item"><svg width="16" height="12" viewBox="0 0 16 12"><rect width="16" height="12" fill="#fff"/><path d="M0 0l8 7 8-7" fill="none" stroke="#9c1b20" stroke-width="1.5"/></svg><span>hello@vellorabistro.example</span></div>
  <div class="socials" style="position:static;color:#fff;margin-left:30px"><span></span><span></span><span></span><span></span><span></span></div>
</address>
<div class="copyright">Copyright © Vellora Bistro</div>

</body>
</html>
```